Construction site banner with out Company information

I need a banner 4' tall and 6' wide, I want the banner to look very similar to the photo I uploaded from LumaDraw, make the person as life like as possible, I like the eyes to pop and be blue, and the hard hat orange, with the rest black and white, I have included our logo to use on the banner as well. Include the following:
Company Name: Brelvo Staffing
Temp Employees
General and Skilled Trades
Workers Comp and Payroll Coverage
www.tmkriv.com

Target Market(s)

Construction Companies

Requirements
Nice to have
• Realistic Person, bright blue eyes, orange hard hat
Should not have
• cartoon looking person

```html
<!DOCTYPE html>
<html lang="en">
<head>
<meta charset="utf-8">
<title>Brelvo Staffing – Site Banner</title>
<link rel="stylesheet" href="https://fonts.googleapis.com/css2?family=Bebas+Neue&family=Oswald:wght@600&family=Allura&display=swap">
<style>
  :root {
    --ink: #050505;
    --paper: #ffffff;
    --orange: #f5911e;
    --orange-deep: #f05a28;
    --stage: #a6a39c;
    --photo-dark: #050505;
    --photo-mid: #2e2724;
    --photo-warm: #6e5f57;
  }
  * { margin: 0; padding: 0; box-sizing: border-box; }
  html, body {
    width: 1200px;
    height: 869px;
    overflow: hidden;
    background: var(--stage);
  }
  .banner {
    position: absolute;
    left: 0;
    top: 34px;
    width: 1200px;
    height: 800px;
    background: var(--paper);
    overflow: hidden;
  }
  .banner-shapes {
    position: absolute;
    inset: 0;
    width: 1200px;
    height: 800px;
  }
  .brand-name {
    position: absolute;
    left: 32px;
    top: 84px;
    font-family: "Bebas Neue", sans-serif;
    font-size: 76px;
    line-height: 1;
    color: var(--orange);
    letter-spacing: 1px;
  }
  .tagline {
    position: absolute;
    left: 32px;
    top: 224px;
    font-family: "Bebas Neue", sans-serif;
    font-size: 90px;
    line-height: 1;
    letter-spacing: 0.5px;
    color: var(--ink);
  }
  .headline {
    position: absolute;
    left: 33px;
    font-family: "Bebas Neue", sans-serif;
    font-size: 142px;
    line-height: 1;
    color: var(--paper);
  }
  .headline-general { top: 315px; }
  .headline-trades { top: 428px; }
  .headline-joiner {
    position: absolute;
    left: 440px;
    top: 318px;
    font-family: "Allura", cursive;
    font-size: 140px;
    line-height: 1;
    color: var(--orange);
    transform: rotate(-4deg);
    transform-origin: left bottom;
  }
  .coverage {
    position: absolute;
    left: 34px;
    top: 564px;
    font-family: "Oswald", sans-serif;
    font-weight: 600;
    font-size: 56px;
    line-height: 57px;
    letter-spacing: 3px;
    color: var(--ink);
    text-transform: uppercase;
  }
  .web {
    position: absolute;
    left: 33px;
    top: 708px;
    display: flex;
    align-items: center;
    gap: 18px;
  }
  .web-icon { width: 78px; height: 78px; }
  .web-address {
    font-family: "Bebas Neue", sans-serif;
    font-size: 87px;
    line-height: 1;
    color: var(--paper);
    padding-top: 6px;
  }
</style>
</head>
<body>
<main class="banner">
  <svg class="banner-shapes" viewBox="0 0 1200 800">
    <defs>
      <linearGradient id="accentSweep" x1="0" y1="0" x2="0" y2="1">
        <stop offset="0" stop-color="#ffffff"/>
        <stop offset="0.35" stop-color="var(--orange)"/>
        <stop offset="1" stop-color="var(--orange)"/>
      </linearGradient>
      <linearGradient id="footerBand" x1="0" y1="0" x2="0" y2="1">
        <stop offset="0" stop-color="#f37d2c"/>
        <stop offset="1" stop-color="var(--orange-deep)"/>
      </linearGradient>
      <linearGradient id="photoTone" x1="0" y1="0" x2="1" y2="0">
        <stop offset="0" stop-color="var(--photo-dark)"/>
        <stop offset="0.45" stop-color="var(--photo-mid)"/>
        <stop offset="1" stop-color="var(--photo-warm)"/>
      </linearGradient>
    </defs>

    <rect class="coverage-band" x="0" y="559" width="760" height="134" fill="var(--orange)"/>
    <rect class="web-band" x="0" y="693" width="760" height="107" fill="url(#footerBand)"/>
    <rect class="headline-band" x="0" y="311" width="727" height="248" fill="var(--ink)"/>

    <path class="accent-sweep" d="M692,0 Q450,400 694,800 L701,800 Q480,420 748,0 Z" fill="url(#accentSweep)"/>

    <path class="photo-area" role="img"
          aria-label="Photo: realistic close-up of a construction worker with a dusty face, bright blue eyes and an orange hard hat, on a black background"
          d="M748,0 Q480,420 701,800 L1200,800 L1200,0 Z" fill="url(#photoTone)"/>
  </svg>

  <div class="brand-name">Brelvo Staffing</div>

  <div class="tagline">Temp Employees</div>

  <div class="headline headline-general">General</div>
  <div class="headline headline-trades">Skilled Trades</div>
  <div class="headline-joiner">and</div>

  <p class="coverage">Workers Comp and<br>Payroll Coverage</p>

  <div class="web">
    <svg class="web-icon" viewBox="0 0 80 80" aria-hidden="true">
      <g fill="none" stroke="var(--ink)" stroke-width="6">
        <circle cx="40" cy="40" r="35"/>
        <ellipse cx="40" cy="40" rx="15" ry="35"/>
        <line x1="40" y1="5" x2="40" y2="75"/>
        <line x1="5" y1="40" x2="75" y2="40"/>
        <path d="M11,22 H69 M11,58 H69"/>
      </g>
    </svg>
    <span class="web-address">www.tmkriv.com</span>
  </div>
</main>
</body>
</html>
```